Tidewell Marketing company is looking for a web page design

Your projects should contain:

1. Header: Logo provided by us.
2. Top nav bar: offer, about us, experience, contact.
3. “Choose language” button.
4. Main section: panoramic picture (static, professional, modern).
5. Below section: 3 blocks (image+title+description), which represent our 3 main activities (titles):
• Market Research,
• Marketing Plans,
• Marketing Project.
6. ‘Contact us’ form – Message (text: “Write your message and give us details about your company and activities”), Email, SEND).
7. Page footer: (4 section: Contact, Social Media, Blog, Partners).
Updates

Hello!

I uploaded new file 'general_look', which is our idea how the page should generally look like.

BUT! it doesn't mean that your projects should look exactly like this project e.g.:
* titles Market Research, Marketing Plans, Marketing Project can be above these: Image 1,2,3.
* everything doesn't have to be in square and rectangle shape. You can try to manipulate with blocks and can add elipse elemnts or something similar.

We will appreciate your innovative ideas. Just wanted to give you general plan of the site and ilustrate all elements that we require.

Best Regards,
Benedek

IMPORTENT

Please remember that the main picture should be panoramic. Please do not close it in frame.

Target Market(s)

Small and middle sized companies, which would like to export their goods and services abroad and are interested in raising funds from Northgate Trade Council to expand their activities. These are rather industrial companies with low level of innovativeness. Our mission is to build image of the client’s company and increase awareness of their products to improve their competitiveness and innovativeness.

Industry/Entity Type

It Company

Requirements
Must have
• 1. Create designs of main page and subpage.
2. Subpage: Logo, Header, language button, place for article, navigation menu on the right side - below it “contact us” button , footer on the bottom. (In this section we are looking mainly for the design of the header and navigation menu).
3. The whole design should be a series of horizontal blocks.
4. Your projects should be associated with features such as: Reliability, Security, Professionalism, Openness, Uniqueness.
5. The design should be simple, fresh, readable, easy to use and should create a feeling of high quality services.
6. Possibility to change the panoramic picture (separate layer in a graphic file).
7. All pictures and blocks should be static, no movements.
8. Style of the page should be compliant with the logo design, font: Swiss.
9. Designs that we like: http://www.fernvale-studio.pl/, http://www.plumquarry.com/.
Should not have
• There shouldn’t be any distractions and not matching parts (whole design should be compact and easy to interpret and remember).

```html
<!DOCTYPE html>
<html lang="en">
<head>
<meta charset="utf-8">
<title>Tidewell Marketing</title>
<link rel="stylesheet" href="https://fonts.googleapis.com/css2?family=Arvo:wght@700&family=Open+Sans:ital,wght@0,400;0,700;1,400;1,700&family=Roboto+Condensed:wght@700&display=swap">
<style>
:root{
  --navy:#0c2134;
  --navy-tab:#071522;
  --logo-bg:#f1eeea;
  --brand:#1d4b70;
  --sand:#f2eee9;
  --card:#e0d9d4;
  --card-edge:#c9c1bb;
  --slate:#4c6d79;
  --btn-top:#7896a1;
  --btn-bottom:#4e6e7a;
  --ink:#2a2a2a;
  --night:#151515;
  --pale:#e9e5e1;
  --muted:#8d8d8d;
  --footer:#474747;
  --footer-link:#a3a3a3;
  --white:#ffffff;
  --icon-a:#cfd9dc;
  --icon-b:#bccbd0;
}
*{margin:0;padding:0;box-sizing:border-box}
html,body{width:863px;height:1200px;overflow:hidden}
body{position:relative;background:var(--sand);font-family:"Open Sans",Arial,sans-serif;color:var(--ink)}
.abs{position:absolute}
.head-font{font-family:"Roboto Condensed",Arial,sans-serif;font-weight:700;text-transform:uppercase;letter-spacing:.2px}

/* header */
.header{left:0;top:0;width:863px;height:103px;background:var(--navy)}
.logo-box{left:105px;top:0;width:246px;height:131px;background:var(--logo-bg);z-index:3;box-shadow:0 2px 6px rgba(0,0,0,.25);display:flex;align-items:center;justify-content:center;gap:8px}
.logo-mark{width:22px;height:22px;border-radius:50%;background:var(--brand)}
.logo-name{font-family:"Open Sans",Arial,sans-serif;font-weight:700;font-size:19px;color:var(--brand);letter-spacing:-.2px}
.lang{right:125px;top:43px;font-size:11.5px;color:var(--white);text-transform:uppercase}
.nav-tab{left:363px;top:69px;width:81px;height:46px;background:var(--navy-tab);z-index:2}
.nav{top:84px;left:0;width:863px;z-index:3;font-size:15px;color:var(--white)}
.nav span{position:absolute;white-space:nowrap}

/* hero */
.hero{left:0;top:103px;width:863px;height:347px;background:
  radial-gradient(ellipse 120px 60px at 320px 250px,rgba(231,98,40,.55),transparent),
  radial-gradient(ellipse 200px 70px at 620px 240px,rgba(226,90,36,.5),transparent),
  radial-gradient(ellipse 150px 90px at 120px 170px,rgba(205,70,40,.45),transparent),
  linear-gradient(180deg,#3a2a2a 0%,#4b3330 30%,#2f2a30 55%,#5a3b2c 80%,#3e2a24 100%)}
.hero-text{right:125px;top:283px;width:360px;text-align:right;font-family:"Arvo",Georgia,serif;font-weight:700;font-size:15.5px;line-height:20px;color:var(--white);text-shadow:0 1px 3px rgba(0,0,0,.7)}
.dots{left:661px;top:386px;display:flex;gap:5px}
.dots i{display:block;width:13px;height:13px;border-radius:50%;background:rgba(255,255,255,.45)}
.dots i:first-child{background:var(--white)}

/* services */
.card{top:420px;width:198px;height:278px;background:var(--card);border:1px solid var(--card-edge);border-radius:4px;text-align:center;box-shadow:0 1px 3px rgba(0,0,0,.12)}
.card-title{margin-top:14px;font-size:17px;line-height:19px;color:var(--slate)}
.card-icon{display:block;margin:16px auto 0;width:84px;height:84px;border-radius:6px;background:linear-gradient(160deg,var(--icon-a),var(--icon-b))}
.card-text{margin-top:12px;font-size:12.5px;line-height:15px;color:var(--ink)}
.btn{display:block;height:24px;border-radius:2px;background:linear-gradient(var(--btn-top),var(--btn-bottom));color:var(--white);font-size:13px;line-height:24px;text-align:center}
.card .btn{position:absolute;left:31px;top:221px;width:139px}

/* contact */
.contact{left:0;top:728px;width:863px;height:223px;background:var(--night)}
.label{font-size:17px;color:var(--pale)}
.intro{left:108px;top:784px;font-size:12px;line-height:15.5px;font-style:italic;color:var(--pale)}
.field-name{font-weight:700;font-size:11.5px;color:var(--pale)}
.field-value{font-weight:700;font-style:italic;font-size:11.5px;color:var(--muted);letter-spacing:.3px}
.email-input{left:539px;top:786px;width:197px;height:41px;background:var(--pale);border-radius:3px}
.send{left:600px;top:838px;width:114px;height:24px;font-size:12px}

/* footer */
.footer{left:0;top:951px;width:863px;height:249px;background:var(--footer)}
.foot-head{font-size:15px;color:var(--pale)}
.foot-list{list-style:none}
.foot-list li{height:21px;font-size:11.5px;color:var(--footer-link);text-transform:uppercase;display:flex;align-items:center;gap:3px;white-space:nowrap}
.bullet{width:8px;height:8px;border-radius:50%;background:#a9c7d2;flex:none}
.social{list-style:none}
.social li{display:flex;align-items:center;gap:6px;font-size:9px;line-height:10px;color:var(--pale);margin-bottom:6px;width:120px}
.social .mark{width:14px;height:14px;border-radius:50%;background:var(--pale);flex:none}
.copyright{left:0;top:1146px;width:863px;text-align:center;font-size:12px;color:var(--pale)}
.copyright b{display:inline-block;width:13px;height:13px;border:1px solid var(--pale);border-radius:50%;font-size:9px;line-height:11px;font-weight:400;margin-right:6px;vertical-align:-1px}
</style>
</head>
<body>

<header>
  <div class="abs header"></div>
  <div class="abs logo-box"><span class="logo-mark"></span><span class="logo-name">Tidewell Marketing</span></div>
  <div class="abs lang">English / Polish</div>
  <div class="abs nav-tab"></div>
  <nav class="abs nav head-font">
    <span style="left:385px">Offer</span>
    <span style="left:459px">About us</span>
    <span style="left:563px">Experience</span>
    <span style="left:671px">Contact</span>
  </nav>
</header>

<section>
  <div class="abs hero" role="img" aria-label="Panoramic night photograph of an industrial harbour with cranes and orange dock lights reflected on the water"></div>
  <p class="abs hero-text">Lorem ipsum dolor sit amet, consectetur adipisicing elit, sed do eiusmod tempor incididunt ut labore</p>
  <div class="abs dots"><i></i><i></i><i></i></div>
</section>

<section>
  <article class="abs card" style="left:105px">
    <h2 class="card-title head-font">Market<br>Research</h2>
    <div class="card-icon" role="img" aria-label="Illustration of a computer monitor showing research charts"></div>
    <p class="card-text">Lorem ipsum dolor sit amet,<br>consectetur adipisicing elit,<br>sed do eiusmod tempor</p>
    <a class="btn head-font">Read more</a>
  </article>

  <article class="abs card" style="left:324px">
    <h2 class="card-title head-font">Marketing<br>Plans</h2>
    <div class="card-icon" role="img" aria-label="Illustration of a clipboard with a planning checklist"></div>
    <p class="card-text">Lorem ipsum dolor sit amet,<br>consectetur adipisicing elit,<br>sed do eiusmod tempor</p>
    <a class="btn head-font">Read more</a>
  </article>

  <article class="abs card" style="left:540px">
    <h2 class="card-title head-font">Marketing<br>Project</h2>
    <div class="card-icon" role="img" aria-label="Illustration of a spade symbolising a project groundbreaking"></div>
    <p class="card-text">Lorem ipsum dolor sit amet,<br>consectetur adipisicing elit,<br>sed do eiusmod tempor</p>
    <a class="btn head-font">Read more</a>
  </article>
</section>

<section>
  <div class="abs contact"></div>
  <h3 class="abs label head-font" style="left:107px;top:757px">Your message</h3>
  <p class="abs intro">Sed ut perspiciatis unde omnis iste<br>natus error sit voluptatem<br>accusantium doloremque</p>
  <h3 class="abs label head-font" style="left:104px;top:858px">Details of your company</h3>
  <span class="abs field-name" style="left:109px;top:891px">NAME :</span>
  <span class="abs field-value" style="left:107px;top:907px">LOREM IPSUM</span>
  <span class="abs field-name" style="left:284px;top:886px">BUSINESS TYPE :</span>
  <span class="abs field-value" style="left:279px;top:903px">EXPORT / IMPORT</span>
  <h3 class="abs label head-font" style="right:125px;top:757px">Your email address</h3>
  <div class="abs email-input"></div>
  <a class="abs btn send head-font">Send</a>
</section>

<footer>
  <div class="abs footer"></div>
  <h4 class="abs foot-head head-font" style="left:107px;top:979px">Contact us</h4>
  <h4 class="abs foot-head head-font" style="left:233px;top:979px">Partners</h4>
  <ul class="abs foot-list" style="left:233px;top:998px">
    <li><span class="bullet"></span>Doloremque laudentium</li>
    <li><span class="bullet"></span>Doloremque laudentium</li>
    <li><span class="bullet"></span>Doloremque laudentium</li>
    <li><span class="bullet"></span>Doloremque laudentium</li>
  </ul>
  <h4 class="abs foot-head head-font" style="left:422px;top:979px">Blog</h4>
  <ul class="abs foot-list" style="left:422px;top:998px">
    <li><span class="bullet"></span>Doloremque laudentium</li>
    <li><span class="bullet"></span>Doloremque laudentium</li>
    <li><span class="bullet"></span>Doloremque laudentium</li>
    <li><span class="bullet"></span>Doloremque laudentium</li>
  </ul>
  <h4 class="abs foot-head head-font" style="left:619px;top:979px">Social media</h4>
  <ul class="abs social" style="left:619px;top:1000px">
    <li><span class="mark"></span>Like us in Chatterly</li>
    <li><span class="mark"></span>Follow us in Chirpline</li>
    <li><span class="mark"></span>Stay connected with us through Workfold</li>
  </ul>
  <p class="abs copyright"><b>c</b>copyright tidewellmarketing 2012</p>
</footer>

</body>
</html>
```